KLVT, Inc.
Continental Meridian Holdings Group
Creative Brief
Corporate
H. Daniel Morrow, Ph.D.
Chief Executive Office
4172 South Birch Meadow Lane, Suite 300 Memphis, TN 38125
dr.danielmorrow@fernmail.example

```html
<!DOCTYPE html>
<html lang="en">
<head>
<meta charset="utf-8">
<title>KLVT, Inc. – Stationery Concepts</title>
<link href="https://fonts.googleapis.com/css2?family=Montserrat:wght@700&family=Open+Sans:wght@400;600&family=Libre+Baskerville&display=swap" rel="stylesheet">
<style>
  :root{
    --board:#3b3b3d;
    --paper:#ffffff;
    --navy:#1f3f8f;
    --green:#1e9a6a;
    --ink:#4a4f5a;
    --faint:#dfe5ef;
    --caption:#b9b9b9;
  }
  *{margin:0;padding:0;box-sizing:border-box}
  html,body{width:1200px;height:427px;overflow:hidden;background:var(--board)}
  .board{position:relative;width:1200px;height:427px;font-family:"Open Sans",sans-serif}
  .piece{position:absolute;background:var(--paper);box-shadow:0 2px 6px rgba(0,0,0,.45);overflow:hidden}
  .caption{position:absolute;font-family:"Libre Baskerville",serif;font-size:7px;color:var(--caption);text-align:center}
  .brand{display:flex;align-items:center;gap:4px}
  .brand-dot{border-radius:50%;background:var(--green)}
  .brand-name{font-family:"Montserrat",sans-serif;font-weight:700;color:var(--navy);line-height:1}
  .brand-tag{font-size:4px;color:var(--ink);margin-top:1px}
  .presenter{position:absolute;left:24px;top:96px}
  .presenter .brand-dot{width:18px;height:18px}
  .presenter .brand-name{font-size:30px}
  .presenter .brand-tag{font-size:6px;color:#cfd3da}
  .presenter-title{position:absolute;left:24px;top:186px;font-family:"Libre Baskerville",serif;font-size:11px;color:#e6e6e6}
  .card{left:24px;top:216px;width:150px;height:88px}
  .card .brand{position:absolute;left:10px;top:10px}
  .card .brand-dot{width:9px;height:9px}
  .card .brand-name{font-size:16px}
  .card-band{position:absolute;left:0;bottom:0;width:150px;height:40px}
  .card-text{position:absolute;right:8px;bottom:7px;color:#fff;font-size:4.5px;line-height:1.45;text-align:left;width:84px}
  .card-text b{font-weight:600;font-size:5px}
  .letterhead{top:31px;width:285px;height:365px}
  .letterhead .brand{position:absolute;left:14px;top:14px}
  .letterhead .brand-dot{width:10px;height:10px}
  .letterhead .brand-name{font-size:17px}
  .lh-contact{position:absolute;right:12px;top:15px;width:90px;font-size:3.6px;line-height:1.5;color:var(--ink)}
  .lh-mark{position:absolute;left:72px;top:110px;width:140px;height:140px;border-radius:50%;background:var(--faint);opacity:.7}
  .lh-wave{position:absolute;left:0;bottom:0;width:285px;height:34px}
  .lh-footer{position:absolute;bottom:5px;left:0;width:100%;text-align:center;font-size:3.6px;color:#fff}
  .envelope{left:828px;width:360px}
  .env-back svg{display:block}
  .env-front{top:257px;height:127px}
  .env-front .brand{position:absolute;left:12px;top:10px}
  .env-front .brand-dot{width:8px;height:8px}
  .env-front .brand-name{font-size:14px}
  .env-front .env-address{position:absolute;left:12px;top:34px;font-size:3.6px;color:var(--ink);width:90px;line-height:1.5}
  .env-front .lh-mark{left:150px;top:20px;width:80px;height:80px}
  .env-front .lh-wave{width:360px;height:28px}
</style>
</head>
<body>
<div class="board">

  <div class="presenter">
    <div class="brand"><span class="brand-dot"></span><span class="brand-name" style="color:#fff">KLVT</span></div>
    <div class="brand-tag">Continental Meridian Holdings Group</div>
  </div>
  <div class="presenter-title">Stationery Concepts</div>

  <div class="piece card">
    <div class="brand"><span class="brand-dot"></span><div><div class="brand-name">KLVT</div><div class="brand-tag">Continental Meridian Holdings Group</div></div></div>
    <svg class="card-band" viewBox="0 0 150 40" preserveAspectRatio="none">
      <path d="M0 14 Q60 2 150 8 L150 40 L0 40Z" fill="var(--green)"/>
      <path d="M0 18 Q60 6 150 12 L150 40 L0 40Z" fill="var(--navy)"/>
    </svg>
    <div class="card-text"><b>H. Daniel Morrow, Ph.D.</b><br>Chief Executive Office<br>Tel 901.555.0142<br>dr.danielmorrow@fernmail.example</div>
  </div>
  <div class="caption" style="left:24px;top:318px;width:150px">Business Card</div>

  <div class="piece letterhead" style="left:202px">
    <div class="brand"><span class="brand-dot"></span><div><div class="brand-name">KLVT</div><div class="brand-tag">Continental Meridian Holdings Group</div></div></div>
    <div class="lh-contact">4172 South Birch Meadow Lane, Suite 300<br>Memphis, TN 38125<br>Tel 901.555.0142<br>dr.danielmorrow@fernmail.example</div>
    <div class="lh-mark"></div>
    <svg class="lh-wave" viewBox="0 0 285 34" preserveAspectRatio="none">
      <path d="M0 6 Q140 22 285 4 L285 34 L0 34Z" fill="var(--green)"/>
      <path d="M0 12 Q140 26 285 10 L285 34 L0 34Z" fill="var(--navy)"/>
    </svg>
    <div class="lh-footer">www.klvt.example</div>
  </div>
  <div class="caption" style="left:202px;top:404px;width:285px">Letterhead Letter A</div>

  <div class="piece letterhead" style="left:506px">
    <div class="brand"><span class="brand-dot"></span><div><div class="brand-name">KLVT</div><div class="brand-tag">Continental Meridian Holdings Group</div></div></div>
    <div class="lh-contact">4172 South Birch Meadow Lane, Suite 300<br>Memphis, TN 38125<br>Tel 901.555.0142<br>dr.danielmorrow@fernmail.example</div>
    <div class="lh-mark"></div>
    <svg class="lh-wave" viewBox="0 0 285 34" preserveAspectRatio="none">
      <path d="M0 6 Q140 22 285 4 L285 34 L0 34Z" fill="var(--green)"/>
      <path d="M0 12 Q140 26 285 10 L285 34 L0 34Z" fill="var(--navy)"/>
    </svg>
    <div class="lh-footer">www.klvt.example</div>
  </div>
  <div class="caption" style="left:506px;top:404px;width:285px">Letterhead Letter B</div>

  <div class="piece envelope env-back" style="top:24px;height:72px">
    <svg viewBox="0 0 360 72" width="360" height="72">
      <path d="M0 0 L360 0 L360 8 L190 60 Q180 64 170 60 L0 8Z" fill="var(--green)"/>
      <circle cx="180" cy="46" r="5" fill="#fff"/>
    </svg>
  </div>
  <div class="piece envelope env-back" style="top:100px;height:68px">
    <svg viewBox="0 0 360 68" width="360" height="68">
      <path d="M0 0 L360 0 L360 8 L190 54 Q180 58 170 54 L0 8Z" fill="var(--navy)"/>
      <circle cx="180" cy="40" r="5" fill="#fff"/>
    </svg>
  </div>
  <div class="piece envelope env-back" style="top:178px;height:76px">
    <svg viewBox="0 0 360 76" width="360" height="76">
      <path d="M0 0 L180 50 L360 0" fill="none" stroke="#d3d6dc" stroke-width="1"/>
      <path d="M0 76 L150 40 M360 76 L210 40" fill="none" stroke="#e2e4e8" stroke-width="1"/>
      <circle cx="180" cy="44" r="5" fill="var(--green)"/>
    </svg>
  </div>
  <div class="piece envelope env-front">
    <div class="brand"><span class="brand-dot"></span><div><div class="brand-name">KLVT</div><div class="brand-tag">Continental Meridian Holdings Group</div></div></div>
    <div class="env-address">4172 South Birch Meadow Lane, Suite 300<br>Memphis, TN 38125</div>
    <div class="lh-mark"></div>
    <svg class="lh-wave" viewBox="0 0 360 28" preserveAspectRatio="none">
      <path d="M0 6 Q180 20 360 3 L360 28 L0 28Z" fill="var(--green)"/>
      <path d="M0 11 Q180 24 360 8 L360 28 L0 28Z" fill="var(--navy)"/>
    </svg>
  </div>
  <div class="caption" style="left:828px;top:404px;width:360px">Envelopes Normal Back</div>

</div>
</body>
</html>
```